Business Card Design Project

Require a business card for a swing band called "Velvet Brass Parade". We are a 6 piece band that performs at events and corporate functions. Our music is great for dancing to or just providing a classy background atmosphere for people to enjoy. Final design should communicate professionalism and style with a hint of fun.

Sorry, just realised that it needs to be single sided only. Also, no rounded edges.

Industry/Entity Type

Events

Requirements
Must have
• Contact number: 0438 216 903
email address: velvetbrassparade@mailbox-demo.net
Website details: www.velvetbrassparade-demo.com

```html
<!DOCTYPE html>
<html lang="en">
<head>
<meta charset="utf-8">
<title>Velvet Brass Parade – Business Cards</title>
<link rel="stylesheet" href="https://fonts.googleapis.com/css2?family=Exo+2:wght@500;700&display=swap">
<style>
  :root {
    --page-bg: #e9e7ea;
    --text-light: #ffffff;
    --magenta-deep: #6e1f86;
    --magenta-mid: #b4108f;
    --magenta-hot: #ec0a8c;
    --magenta-wordmark: #5e1a78;
    --indigo-deep: #16257a;
    --indigo-mid: #2a12d8;
    --indigo-hot: #3b14f2;
    --indigo-wordmark: #1b2268;
    --splash-light: rgba(255, 255, 255, 0.85);
  }

  * { box-sizing: border-box; margin: 0; padding: 0; }

  html, body {
    width: 1200px;
    height: 534px;
    overflow: hidden;
    background: var(--page-bg);
    font-family: "Exo 2", sans-serif;
  }

  .stage {
    position: relative;
    width: 1200px;
    height: 534px;
  }

  .card {
    position: absolute;
    top: 119px;
    width: 517px;
    height: 295px;
    overflow: hidden;
    color: var(--text-light);
  }

  .card--magenta {
    left: 62px;
    background:
      radial-gradient(ellipse 60% 80% at 62% 30%, var(--magenta-hot) 0%, rgba(236, 10, 140, 0) 70%),
      linear-gradient(90deg, var(--magenta-deep) 0%, var(--magenta-mid) 45%, var(--magenta-hot) 60%, var(--magenta-deep) 100%);
    --wordmark: var(--magenta-wordmark);
  }

  .card--indigo {
    left: 622px;
    background:
      radial-gradient(ellipse 60% 80% at 60% 30%, var(--indigo-hot) 0%, rgba(59, 20, 242, 0) 70%),
      linear-gradient(90deg, var(--indigo-deep) 0%, var(--indigo-mid) 45%, var(--indigo-hot) 60%, var(--indigo-deep) 100%);
    --wordmark: var(--indigo-wordmark);
  }

  .card__splash {
    position: absolute;
    inset: 0;
    width: 517px;
    height: 295px;
  }

  .card__wordmark {
    position: absolute;
    left: 100px;
    top: 22px;
    width: 330px;
    font-weight: 700;
    font-size: 44px;
    line-height: 0.98;
    color: var(--wordmark);
    text-align: center;
  }

  .card__contact {
    position: absolute;
    right: 34px;
    top: 186px;
    text-align: right;
  }

  .card__name {
    font-weight: 700;
    font-size: 15px;
    line-height: 17px;
  }

  .card__role {
    font-weight: 500;
    font-size: 11px;
    line-height: 13px;
    margin-bottom: 8px;
  }

  .card__details {
    list-style: none;
    font-weight: 500;
    font-size: 12px;
    line-height: 16px;
  }
</style>
</head>
<body>
<main class="stage">

  <article class="card card--magenta">
    <svg class="card__splash" viewBox="0 0 517 295" role="img" aria-label="White paint splatter spray across the left side and behind the band name">
      <defs>
        <radialGradient id="splash-left-m" cx="0" cy="1" r="0.9">
          <stop offset="0" stop-color="#ffffff" stop-opacity="0.9"/>
          <stop offset="0.5" stop-color="#ffffff" stop-opacity="0.35"/>
          <stop offset="1" stop-color="#ffffff" stop-opacity="0"/>
        </radialGradient>
        <radialGradient id="splash-top-m" cx="0.5" cy="0.5" r="0.5">
          <stop offset="0" stop-color="#ffffff" stop-opacity="0.45"/>
          <stop offset="1" stop-color="#ffffff" stop-opacity="0"/>
        </radialGradient>
      </defs>
      <rect x="0" y="0" width="260" height="295" fill="url(#splash-left-m)"/>
      <ellipse cx="290" cy="95" rx="200" ry="95" fill="url(#splash-top-m)"/>
    </svg>
    <p class="card__wordmark">Velvet Brass Parade</p>
    <div class="card__contact">
      <p class="card__name">Marlo Quince</p>
      <p class="card__role">position</p>
      <ul class="card__details">
        <li>telephone: 0438 216 903</li>
        <li>email: velvetbrassparade@mailbox-demo.net</li>
        <li>website: www.velvetbrassparade-demo.com</li>
      </ul>
    </div>
  </article>

  <article class="card card--indigo">
    <svg class="card__splash" viewBox="0 0 517 295" role="img" aria-label="White paint splatter spray across the left side and behind the band name">
      <defs>
        <radialGradient id="splash-left-i" cx="0" cy="1" r="0.9">
          <stop offset="0" stop-color="#ffffff" stop-opacity="0.9"/>
          <stop offset="0.5" stop-color="#ffffff" stop-opacity="0.35"/>
          <stop offset="1" stop-color="#ffffff" stop-opacity="0"/>
        </radialGradient>
        <radialGradient id="splash-top-i" cx="0.5" cy="0.5" r="0.5">
          <stop offset="0" stop-color="#ffffff" stop-opacity="0.45"/>
          <stop offset="1" stop-color="#ffffff" stop-opacity="0"/>
        </radialGradient>
      </defs>
      <rect x="0" y="0" width="260" height="295" fill="url(#splash-left-i)"/>
      <ellipse cx="290" cy="95" rx="200" ry="95" fill="url(#splash-top-i)"/>
    </svg>
    <p class="card__wordmark">Velvet Brass Parade</p>
    <div class="card__contact">
      <p class="card__name">Marlo Quince</p>
      <p class="card__role">position</p>
      <ul class="card__details">
        <li>telephone: 0438 216 903</li>
        <li>email: velvetbrassparade@mailbox-demo.net</li>
        <li>website: www.velvetbrassparade-demo.com</li>
      </ul>
    </div>
  </article>

</main>
</body>
</html>
```